Need Epic Web Banner for New Site

We need a banner for our web page. We are BrightStrydo.com, think of us as the Pondelly of the highest quality sports nutrition supplements on the web. Our site is under construction, if you visit our site, this banner will go at the very top above the menu bar. We are marketing supplements a different way then most; we are staying away from hulked out guys on steroids & gimmick magic pills/ slogans. We are all about clean quality products with less ingredients.

We are attaching our logo/ symbol & a text we made in AI for a point of reference. Please help us bring our site and vision of BrightStrydo to life!

We are not married to the colors but GREEN is a must!
Updates

Disregard previous message about Tova's entry. This platform does not allow me to delet comments I post.

Target Market(s)

Heath Consious, Health Seekers, Active Fit People, Gym Rats, Rock Climbers

Industry/Entity Type

Nutrition

Font styles to use
Other font styles liked:
• Semplicita

Colors
33b8a4
00a990
86cfc6

Requirements
Must have
• For text In addition to BrightStrydo.com we'd like "Not all supplements are created equal"

```html
<!DOCTYPE html>
<html lang="en">
<head>
<meta charset="utf-8">
<title>BrightStrydo.com – Web Banner</title>
<link rel="stylesheet" href="https://fonts.googleapis.com/css2?family=Questrial&display=swap">
<style>
  :root {
    --stage-bg: #1f1f1f;
    --banner-white: #ffffff;
    --leaf-light: #acd8a7;
    --leaf-deep: #2e8f6a;
    --text-light: #ffffff;
  }
  * { margin: 0; padding: 0; box-sizing: border-box; }
  html, body {
    width: 1200px;
    height: 1000px;
    overflow: hidden;
    background: var(--stage-bg);
  }
  .stage {
    position: relative;
    width: 1200px;
    height: 1000px;
  }
  .banner {
    position: absolute;
    left: 121px;
    top: 339px;
    width: 996px;
    height: 198px;
    background: var(--banner-white);
    overflow: hidden;
  }
  .banner-shapes {
    position: absolute;
    inset: 0;
    width: 996px;
    height: 198px;
  }
  .brand-name {
    position: absolute;
    left: 8px;
    top: 58px;
    font-family: "Questrial", sans-serif;
    font-weight: 400;
    font-size: 52px;
    line-height: 1;
    letter-spacing: 0.5px;
    color: var(--leaf-deep);
    white-space: nowrap;
  }
  .brand-slogan {
    position: absolute;
    left: 11px;
    top: 124px;
    font-family: "Questrial", sans-serif;
    font-size: 18px;
    line-height: 1;
    letter-spacing: 0.3px;
    color: var(--leaf-deep);
    white-space: nowrap;
  }
  .tagline {
    position: absolute;
    left: 500px;
    top: 46px;
    width: 484px;
    text-align: center;
    font-family: "Questrial", sans-serif;
    font-size: 35px;
    line-height: 52px;
    letter-spacing: 0;
    color: var(--text-light);
    text-transform: uppercase;
    white-space: nowrap;
  }
</style>
</head>
<body>
  <main class="stage">
    <section class="banner" aria-label="BrightStrydo.com banner">
      <svg class="banner-shapes" viewBox="0 0 996 198" aria-hidden="true">
        <polygon class="accent-stripe" points="504,0 517,0 414,198 400,198" fill="var(--leaf-deep)"/>
        <polygon class="tagline-panel" points="517,0 996,0 996,198 414,198" fill="var(--leaf-light)"/>
      </svg>
      <h1 class="brand-name">BrightStrydo.com</h1>
      <p class="brand-slogan">Not all supplements are created equal</p>
      <p class="tagline">Clean quality products<br>with less ingredients</p>
    </section>
  </main>
</body>
</html>
```